Web page for a garment manufacturing company

We are clothing manufacturer based in Romania.
With our recent expansion, we have significantly increased our internal capacity, allowing us to take on new partnerships and deliver high-quality production services.
Our expertise includes producing classic coats, blazers, trousers, skirts, dresses, and blouses, though we are flexible and open to working with various other textile products.

Target Market(s)

High-end market and luxury

Industry/Entity Type

Garments Manufacturer

Coding

Coded - Design and coding required

Number of Pages Required

1 page

Colors

Designer to choose only greyscale colors for use in the design.

Requirements
Must have
• Velmora logo from our presentation
Nice to have
• https://www.dorlaque.pt/
Should not have
• prices, wedding dresses, collections

```html
<!DOCTYPE html>
<html lang="en">
<head>
<meta charset="utf-8">
<title>Velmora — Clothing manufacturer</title>
<link href="https://fonts.googleapis.com/css2?family=Jost:wght@300;400;500&display=swap" rel="stylesheet">
<style>
:root{
  --ink:#111111;
  --text:#2b2b2b;
  --muted:#9a9a9a;
  --line:#cfcfcf;
  --band:#efefef;
  --white:#ffffff;
  --black:#000000;
}
*{box-sizing:border-box;margin:0;padding:0}
html,body{width:1200px;height:4345px;overflow:hidden;background:var(--white)}
body{font-family:'Jost',sans-serif;color:var(--text);position:relative}
.abs{position:absolute}
.photo{position:absolute}
.btn{position:absolute;display:flex;align-items:center;justify-content:center;font-size:9px;font-weight:500;color:var(--ink);background:var(--white)}
.btn.outline{border:1px solid var(--ink)}
.btn.grey{background:#e6e6e6}

/* nav */
.nav{position:absolute;left:0;top:0;width:1200px;height:60px;background:var(--white)}
.brand{position:absolute;left:106px;top:14px;font-size:30px;font-weight:400;color:var(--ink);letter-spacing:-.5px}
.menu{position:absolute;left:480px;top:23px;display:flex;gap:0;font-size:9px;color:var(--ink)}
.menu span{display:inline-block}
.nav-cta{position:absolute;left:993px;top:16px;width:100px;height:30px;background:var(--black);color:var(--white);font-size:9px;display:flex;align-items:center;justify-content:center}

/* hero */
.hero{position:absolute;left:0;top:60px;width:1200px;height:525px;background:linear-gradient(100deg,#2a2520 0%,#3e3630 35%,#6b5d55 55%,#8a7a70 70%,#4a3b33 100%)}
.hero h1{position:absolute;left:106px;top:155px;font-size:36px;font-weight:300;color:var(--white);line-height:1.22}
.hero p{position:absolute;left:106px;top:280px;font-size:16px;font-weight:300;color:var(--white);line-height:1.5}

/* welcome */
.eyebrow{font-size:13px;color:var(--muted);font-weight:300}
.welcome-title{position:absolute;left:612px;top:693px;font-size:58px;font-weight:300;color:var(--ink)}
.welcome-lead{position:absolute;left:612px;top:777px;width:400px;font-size:12px;line-height:1.8;color:var(--ink);font-weight:400}
.welcome-body{position:absolute;left:612px;top:858px;width:400px;font-size:10px;line-height:1.9;color:var(--text)}
.stat{position:absolute;font-weight:300}
.stat .k{font-size:10px;color:var(--muted)}
.stat .v{font-size:20px;color:var(--ink)}
.stat .s{font-size:10px;color:var(--muted)}
.slash{position:absolute;width:1px;height:30px;background:#777;transform:rotate(28deg)}

/* mission / vision */
.band{position:absolute;left:0;width:1200px;background:var(--band)}
.h2{position:absolute;font-size:36px;font-weight:300;color:var(--ink)}
.para{position:absolute;font-size:10px;line-height:2.2;color:var(--text)}

/* values */
.value{position:absolute;top:2178px;width:177px;height:128px;background:var(--white);box-shadow:0 0 14px rgba(0,0,0,.07);text-align:center;font-size:12px;color:var(--ink);line-height:1.5}
.value svg{display:block;margin:18px auto 10px}
.value.active{background:var(--black);color:var(--white)}

/* infrastructure */
.tile-label{position:absolute;width:250px;height:34px;background:var(--white);font-size:12px;color:var(--ink);display:flex;align-items:center;justify-content:center}
.tile-line{position:absolute;height:1px;background:#999}

/* community */
.news-label{position:absolute;background:var(--white);font-size:10px;color:var(--ink);padding:6px 12px;width:120px}

/* certifications */
.cert{position:absolute;top:3868px;height:44px;border-radius:6px;background:#e2e2e2}
.dot{position:absolute;top:3934px;width:6px;height:6px;border-radius:50%;background:#c9c9c9}

/* footer */
.footer{position:absolute;left:0;top:4020px;width:1200px;height:325px;background:var(--black);color:var(--white)}
.footer .logo{position:absolute;left:199px;top:70px;font-size:54px;font-weight:300}
.fcol{position:absolute;font-size:10px;line-height:1.9;font-weight:300}
.fcol h4{font-size:11px;font-weight:400;margin-bottom:12px}
.social{position:absolute;left:985px;width:30px;height:30px;border-radius:50%;background:#8c8c8c}
.footer .rule{position:absolute;left:199px;top:262px;width:802px;height:1px;background:#333}
.footer .copy{position:absolute;left:0;width:1200px;top:285px;text-align:center;font-size:9px;color:#cfcfcf}
</style>
</head>
<body>

<header class="nav">
  <div class="brand">Velmora</div>
  <nav class="menu">
    <span style="margin-right:34px;font-weight:500">Home</span>
    <span style="margin-right:34px">About us</span>
    <span style="margin-right:34px">Communication</span>
    <span style="margin-right:34px">Concepts</span>
    <span style="margin-right:34px">News</span>
    <span style="margin-right:34px">Career</span>
    <span>Contact us</span>
  </nav>
  <div class="nav-cta">Get in touch</div>
</header>

<section class="hero" role="img" aria-label="Woman with glasses in a beige coat on a city street">
  <h1>We are clothing manufacturer<br>based in romania.</h1>
  <p>Established in 2005 as a Joint Venture between a<br>local manufacturer and a foreign &nbsp;investor.</p>
  <div class="btn" style="left:106px;top:345px;width:100px;height:30px">Contact us</div>
</section>

<section class="welcome">
  <div class="photo" role="img" aria-label="Woman in a dark blazer standing by a window" style="left:199px;top:658px;width:333px;height:422px;background:linear-gradient(160deg,#8a7c70,#3b3d45 60%,#2a2c33)"></div>
  <div class="abs eyebrow" style="left:612px;top:676px">Welcome to</div>
  <h2 class="welcome-title">Velmora</h2>
  <p class="welcome-lead">VELMORA is a manufacturing company for Ready-to-wear, situated in &nbsp;Focsani, a city with a rich &nbsp;tradition in the clothing industry.</p>
  <p class="welcome-body">The top management is international, and we are proud to have a diverse and dynamic group of professionals from different countries working together. With our optimistic team spirit and passion for high-quality productions, we are ready to take on new &nbsp;challenges and delight our clients with very good results.</p>
  <div class="btn grey" style="left:612px;top:1003px;width:100px;height:30px">Explore more</div>

  <div class="stat" style="left:240px;top:1149px"><span class="k">Manufacturing</span></div>
  <div class="slash" style="left:325px;top:1140px"></div>
  <div class="stat" style="left:282px;top:1170px"><span class="v">100.000</span></div>
  <div class="slash" style="left:294px;top:1203px"></div>
  <div class="stat" style="left:318px;top:1210px"><span class="s">Pieces / month</span></div>

  <div class="stat" style="left:503px;top:1149px"><span class="k">Ladies' garments</span></div>
  <div class="slash" style="left:617px;top:1140px"></div>
  <div class="stat" style="left:578px;top:1170px"><span class="v">75 %</span></div>
  <div class="slash" style="left:574px;top:1203px"></div>
  <div class="stat" style="left:600px;top:1210px"><span class="s">Of the capacity</span></div>

  <div class="stat" style="left:784px;top:1149px"><span class="k">Men's garments</span></div>
  <div class="slash" style="left:893px;top:1140px"></div>
  <div class="stat" style="left:851px;top:1170px"><span class="v">25 %</span></div>
  <div class="slash" style="left:852px;top:1203px"></div>
  <div class="stat" style="left:876px;top:1210px"><span class="s">Of the capacity</span></div>
</section>

<section class="mission-vision">
  <div class="band" style="top:1354px;height:640px"></div>
  <h2 class="h2" style="left:106px;top:1440px">Mission</h2>
  <p class="para" style="left:106px;top:1508px;width:450px">To provide exceptional quality products and services, to meet our customers' expectations while being environmentally and socially responsible in every aspect of our business. Additionally, we recognize and value the importance of our workers, ensuring their well-being and fostering a positive and inclusive work environment.</p>
  <div class="photo" role="img" aria-label="Two pattern makers cutting fabric at a workshop table" style="left:607px;top:1306px;width:482px;height:342px;background:linear-gradient(135deg,#d9dbe0,#a9aeb8 45%,#5f6470 75%,#8d8378)"></div>

  <div class="photo" role="img" aria-label="Clothing rack and a lilac blazer on a dress form" style="left:106px;top:1710px;width:482px;height:344px;background:linear-gradient(120deg,#e9e7e4,#cfc6c0 45%,#b896b8 70%,#efeeec)"></div>
  <h2 class="h2" style="left:637px;top:1797px">Vision</h2>
  <p class="para" style="left:637px;top:1866px;width:440px">To be the leading destination for fashion brands who value both quality and &nbsp;sustainability. By prioritizing the well-being and satisfaction of our workers, we strive &nbsp;to create an environment that fosters innovation, collaboration, and growth, reinforcing &nbsp;our &nbsp;commitment to excellence and sustainable practices.</p>
</section>

<section class="values">
  <h2 class="h2" style="left:0;width:1200px;text-align:center;top:2110px">Velmora value</h2>
  <div class="value" style="left:106px">
    <svg width="40" height="40" viewBox="0 0 40 40" fill="none" stroke="#111" stroke-width="1.4"><circle cx="20" cy="12" r="6"/><path d="M8 36c0-7 5-12 12-12s12 5 12 12"/></svg>
    Prioritize worker<br>well-being</div>
  <div class="value" style="left:309px">
    <svg width="40" height="40" viewBox="0 0 40 40" fill="none" stroke="#111" stroke-width="1.4"><path d="M20 5l3 7 7 1-5 5 1 7-6-3-6 3 1-7-5-5 7-1z"/><path d="M10 36h20M14 30h12"/></svg>
    High-quality products<br>and services</div>
  <div class="value active" style="left:512px">
    <svg width="40" height="40" viewBox="0 0 40 40" fill="none" stroke="#fff" stroke-width="1.4"><circle cx="20" cy="20" r="13"/><path d="M20 7c-5 5-5 21 0 26M20 7c5 5 5 21 0 26M7 20h26"/></svg>
    Environmental<br>responsibility</div>
  <div class="value" style="left:715px">
    <svg width="40" height="40" viewBox="0 0 40 40" fill="none" stroke="#111" stroke-width="1.4"><circle cx="20" cy="17" r="11"/><path d="M12 34h16M20 28v6"/></svg>
    Social<br>responsibility</div>
  <div class="value" style="left:918px">
    <svg width="40" height="40" viewBox="0 0 40 40" fill="none" stroke="#111" stroke-width="1.4"><path d="M20 5a10 10 0 0 0-6 18v5h12v-5a10 10 0 0 0-6-18z"/><path d="M15 32h10M17 36h6"/></svg>
    Innovation and<br>technology</div>
  <div class="btn outline" style="left:550px;top:2348px;width:100px;height:28px">Contact us</div>
</section>

<section class="infrastructure">
  <div class="band" style="top:2450px;height:555px"></div>
  <h2 class="h2" style="left:0;width:1200px;text-align:center;top:2518px">Velmora infrastructure</h2>
  <div class="photo" role="img" aria-label="Office workspace" style="left:0;top:2592px;width:80px;height:312px;background:linear-gradient(180deg,#b9b6b2,#6d6863)"></div>
  <div class="photo" role="img" aria-label="Merchandisers working at computers" style="left:106px;top:2592px;width:311px;height:312px;background:linear-gradient(160deg,#e4e4e2,#9ea3a8 55%,#3e4248)"></div>
  <div class="photo" role="img" aria-label="Pattern makers fitting a grey dress on a form" style="left:443px;top:2592px;width:311px;height:312px;background:linear-gradient(160deg,#d7d4d0,#8e8883 55%,#4a4744)"></div>
  <div class="photo" role="img" aria-label="Brick warehouse building with loading doors" style="left:783px;top:2592px;width:311px;height:312px;background:linear-gradient(180deg,#c9ced4 0%,#c9ced4 35%,#7a5a4a 36%,#4f3d34 80%,#8a8a88)"></div>
  <div class="photo" role="img" aria-label="Production floor" style="left:1120px;top:2592px;width:80px;height:312px;background:linear-gradient(180deg,#c0b8b0,#6b6058)"></div>
  <div class="abs" style="left:918px;top:2578px;width:42px;height:28px;background:#fff;border-radius:14px;font-size:7px;display:flex;align-items:center;justify-content:center;color:#111">&lsaquo; Drag &rsaquo;</div>

  <div class="tile-label" style="left:137px;top:2884px">Merchandisers</div>
  <div class="tile-label" style="left:474px;top:2884px">Pattern, 3D, CAD</div>
  <div class="tile-label" style="left:814px;top:2884px">Warehouse</div>
  <div class="tile-line" style="left:0;top:2926px;width:50px"></div>
  <div class="tile-line" style="left:137px;top:2926px;width:250px"></div>
  <div class="tile-line" style="left:474px;top:2926px;width:250px"></div>
  <div class="tile-line" style="left:814px;top:2926px;width:250px"></div>
  <div class="tile-line" style="left:1150px;top:2926px;width:50px"></div>
</section>

<section class="community">
  <div class="abs eyebrow" style="left:0;width:1200px;text-align:center;top:3076px;font-size:11px">Latest news</div>
  <h2 class="h2" style="left:0;width:1200px;text-align:center;top:3098px">Community activities</h2>
  <div class="photo" role="img" aria-label="Children on a rope course at a summer camp" style="left:307px;top:3180px;width:281px;height:455px;background:linear-gradient(170deg,#6f8a4e,#a39070 50%,#5a6a3e)">
    <div class="news-label" style="left:0;bottom:20px">Summer camp</div>
  </div>
  <div class="photo" role="img" aria-label="Halloween decorated door with pumpkins" style="left:611px;top:3180px;width:281px;height:216px;background:linear-gradient(160deg,#4f6a3c,#7a4a38 55%,#3a2a24)">
    <div class="news-label" style="left:0;bottom:20px">Halloween party</div>
  </div>
  <div class="photo" role="img" aria-label="Christmas crafts on a wooden table" style="left:611px;top:3419px;width:281px;height:216px;background:linear-gradient(150deg,#8a6e58,#b89a82 50%,#6a4f3e)">
    <div class="news-label" style="left:0;bottom:20px">Christmas creativity</div>
  </div>
  <div class="btn grey" style="left:550px;top:3672px;width:100px;height:28px">View all</div>
</section>

<section class="certifications">
  <h2 class="h2" style="left:0;width:1200px;text-align:center;top:3776px">Our certifications</h2>
  <div class="cert" style="left:226px;width:56px"></div>
  <div class="cert" style="left:330px;width:120px"></div>
  <div class="cert" style="left:496px;width:108px"></div>
  <div class="cert" style="left:654px;width:52px;border-radius:50%"></div>
  <div class="cert" style="left:753px;width:86px"></div>
  <div class="cert" style="left:886px;width:86px"></div>
  <div class="dot" style="left:573px;background:#555"></div>
  <div class="dot" style="left:586px"></div>
  <div class="dot" style="left:599px"></div>
  <div class="dot" style="left:612px"></div>
</section>

<footer class="footer">
  <div class="logo">Velmora</div>
  <div class="fcol" style="left:437px;top:62px">
    <h4>Contact Us</h4>
    <div style="font-size:12px">
      <svg width="10" height="10" viewBox="0 0 10 10" fill="#fff"><path d="M2 1l2 2-1 1.5a6 6 0 0 0 2.5 2.5L7 6l2 2-1 1.5C4 9 1 6 .5 2z"/></svg>
      +40 300 410 275</div>
    <div style="margin-top:6px">
      <svg width="10" height="8" viewBox="0 0 10 8" fill="none" stroke="#fff"><rect x=".5" y=".5" width="9" height="7"/><path d="M.5 .5l4.5 4 4.5-4"/></svg>
      info@velmorafashion.com</div>
    <div style="margin-top:6px">
      <svg width="8" height="10" viewBox="0 0 8 10" fill="#fff"><path d="M4 0a4 4 0 0 1 4 4c0 3-4 6-4 6S0 7 0 4a4 4 0 0 1 4-4z"/></svg>
      Romania Focsani Str. Teilor 8,<br>&nbsp;&nbsp;&nbsp;Zip code: 620410</div>
  </div>
  <div class="fcol" style="left:675px;top:62px">
    <h4>Company</h4>
    <div>Home</div><div>About us</div><div>Communication</div><div>Concepts</div><div>News</div>
  </div>
  <div class="fcol" style="left:787px;top:91px">
    <div>Career</div><div>Contact us</div><div>Terms and Conditions</div><div>Privacy Policy</div>
  </div>
  <div class="social" style="top:78px"></div>
  <div class="social" style="top:116px;background:#fff"></div>
  <div class="social" style="top:154px"></div>
  <div class="social" style="top:192px"></div>
  <div class="rule"></div>
  <div class="copy">© 2024 Velmora. All Rights Reserved</div>
</footer>

</body>
</html>
```